Fernway Fitness Direct Mail for Weight Loss Challenge

We need a two-sided direct mail piece made for all three of our fitness facilities that promotes a weight loss challenge. The weight loss challenge (Ripple Past Winter! (our gym is eco-friendly and our logo is a leaf, hence the sprout)) is simple- lose 1 lb, get $20 (up to $200). The challenge is 8 weeks long and they must join before March 31st to be eligible. Attached is our logo, and other direct mail pieces that have been created in the past. We like cleaner looking pieces that do not look busy, but rather clean and effective, with only a few messages. On the front, we'd like this weight loss challenge, and then on the back left, a description of our two membership options- 1. Tally Plan- the more you workout, the less you pay. As Low As $0/month. (the more times you come in, the less your dues are) and 2. Month to Month- $19/month, month to month, with zero long-term contracts. In the middle, the locations as you can see on the other pieces, and then on the right, space for postage like we already have. We would need three pieces created, since these will be going out to three separate locations. The only difference will be the location of, for example, Plainfield highlighted more than the other two locations, and so on.

Fitness

```html
<!DOCTYPE html>
<html lang="en">
<head>
<meta charset="utf-8">
<title>The Weight Loss Challenge – Fernway Fitness</title>
<link href="https://fonts.googleapis.com/css2?family=Teko:wght@400;500&family=Michroma&family=Lato:wght@400;700&family=Montserrat:wght@700&display=swap" rel="stylesheet">
<style>
  :root {
    --page-bg: #e9e9e6;
    --green-deep: #2e8b36;
    --green-mid: #43a63c;
    --green-bright: #8fd53a;
    --green-pale: #b6e36a;
    --lime-text: #c8f03c;
    --ink: #0d0d0d;
    --white: #ffffff;
    --yellow: #f5e626;
    --body-text: #3d3d3d;
  }
  * { margin: 0; padding: 0; box-sizing: border-box; }
  html, body { width: 806px; height: 1200px; overflow: hidden; background: var(--page-bg); }
  .flyer {
    position: absolute; left: 126px; top: 50px; width: 580px; height: 1070px;
    overflow: hidden; background: var(--green-bright);
    box-shadow: 0 6px 20px rgba(0,0,0,.18);
  }
  .flyer-shapes { position: absolute; inset: 0; }
  .headline {
    position: absolute; top: 38px; left: 0; width: 100%; text-align: center;
    font-family: "Teko", sans-serif; font-weight: 500; font-size: 55px; line-height: 1;
    color: var(--white); letter-spacing: .5px; white-space: nowrap;
  }
  .tagline {
    position: absolute; top: 101px; left: 0; width: 100%; text-align: center;
    font-family: "Michroma", sans-serif; font-size: 16px; letter-spacing: 3px;
    color: var(--lime-text); text-transform: uppercase;
  }
  .brand-name {
    position: absolute; left: 306px; top: 373px; width: 136px; text-align: center;
    font-family: "Lato", sans-serif; font-weight: 700; font-size: 15px; letter-spacing: 1.5px;
    color: var(--green-mid); text-transform: uppercase;
  }
  .phone {
    position: absolute; left: 518px; top: 522px; transform: rotate(-90deg); transform-origin: left top;
    display: flex; align-items: center; gap: 10px;
    font-family: "Montserrat", sans-serif; font-weight: 700; font-size: 22px; line-height: 28px; letter-spacing: 1.5px;
    color: var(--white); white-space: nowrap;
  }
  .phone svg { transform: rotate(90deg); flex: none; }
  .offer {
    position: absolute; left: 220px; top: 547px; width: 340px; text-align: center;
    font-family: "Teko", sans-serif; font-size: 27px; line-height: 38px; color: var(--white);
  }
  .challenge {
    position: absolute; right: 30px; top: 607px; width: 440px; text-align: right;
    font-family: "Lato", sans-serif; font-weight: 700; font-size: 24px; line-height: 33px; color: var(--white);
    white-space: nowrap;
  }
  .challenge em { font-style: normal; color: var(--yellow); }
  .about-title {
    position: absolute; left: 374px; top: 729px; width: 186px; text-align: center;
    font-family: "Montserrat", sans-serif; font-weight: 700; font-size: 24px; color: var(--white); letter-spacing: 1px;
  }
  .about-copy {
    position: absolute; right: 30px; top: 785px; width: 345px; text-align: right;
    font-family: "Lato", sans-serif; font-size: 11.6px; line-height: 15px; color: var(--body-text);
  }
  .about-copy p + p { margin-top: 12px; }
  .website {
    position: absolute; right: 30px; top: 1019px; display: flex; align-items: center; gap: 10px;
    font-family: "Montserrat", sans-serif; font-weight: 700; font-size: 15px; letter-spacing: .5px; color: var(--white);
  }
</style>
</head>
<body>
<main class="flyer">
  <svg class="flyer-shapes" width="580" height="1070" viewBox="0 0 580 1070">
    <defs>
      <linearGradient id="header-fill" x1="0" y1="0" x2="0" y2="1">
        <stop offset="0" stop-color="#2c8a35"/><stop offset="1" stop-color="#3f9f3a"/>
      </linearGradient>
      <linearGradient id="lower-fill" x1="0" y1="0" x2="1" y2="1">
        <stop offset="0" stop-color="#7cc934"/><stop offset=".6" stop-color="#9ad93f"/><stop offset="1" stop-color="#6dbb2f"/>
      </linearGradient>
      <linearGradient id="athlete-fill" x1="0" y1="0" x2="1" y2="1">
        <stop offset="0" stop-color="#3a2c26"/><stop offset=".5" stop-color="#7a5443"/><stop offset="1" stop-color="#1d1d1d"/>
      </linearGradient>
      <linearGradient id="trainer-fill" x1="0" y1="0" x2="0" y2="1">
        <stop offset="0" stop-color="#d9b98a"/><stop offset=".45" stop-color="#e9a53a"/><stop offset="1" stop-color="#2a2a2a"/>
      </linearGradient>
    </defs>
    <rect class="lower-panel" x="0" y="0" width="580" height="1070" fill="url(#lower-fill)"/>
    <rect class="header-band" x="0" y="0" width="580" height="200" fill="url(#header-fill)"/>
    <path class="photo-frame" d="M0,200 Q220,110 580,135 L580,520 L0,520 Z" fill="#ffffff"/>
    <path class="photo-side" d="M0,212 Q230,125 580,148 L580,520 L0,520 Z" fill="#a8dd4e"/>
    <path class="athlete-photo" role="img" aria-label="Photo of a man lifting dumbbells in a gym"
          d="M0,215 Q230,130 548,150 Q470,420 330,505 Q160,540 0,470 Z" fill="url(#athlete-fill)"/>
    <path class="photo-edge" d="M0,470 Q160,540 330,505 Q470,420 548,150" fill="none" stroke="#ffffff" stroke-width="8"/>
    <circle class="brand-disc" cx="374" cy="385" r="72" fill="#ffffff"/>
    <circle class="brand-ring" cx="374" cy="385" r="62" fill="none" stroke="#4fb03a" stroke-width="3"/>
    <rect class="offer-bar" x="220" y="545" width="360" height="40" fill="#3f9b34"/>
    <path class="challenge-band" d="M90,590 L580,590 L580,720 L30,720 L90,650 Z" fill="var(--ink)"/>
    <path class="about-tab" d="M374,726 L580,726 L580,762 L350,762 Z" fill="#3f9b34"/>
    <path class="bottom-band" d="M0,930 Q300,1000 580,955 L580,1070 L0,1070 Z" fill="var(--ink)"/>
    <path class="bottom-swoosh" d="M150,980 Q380,1000 580,950" fill="none" stroke="#4fb03a" stroke-width="6"/>
    <rect class="trainer-photo" role="img" aria-label="Photo of a smiling woman in a yellow top holding a dumbbell"
          x="0" y="660" width="175" height="410" rx="70" fill="url(#trainer-fill)"/>
  </svg>

  <h1 class="headline">THE WEIGHT LOSS CHALLENGE</h1>
  <p class="tagline">Ripple Past Winter!</p>

  <div class="brand-name">Fernway Fitness</div>

  <div class="phone">
    <svg width="20" height="20" viewBox="0 0 24 24" aria-hidden="true"><path d="M6.6 10.8a15 15 0 0 0 6.6 6.6l2.2-2.2a1 1 0 0 1 1-.25 11.4 11.4 0 0 0 3.6.57 1 1 0 0 1 1 1V20a1 1 0 0 1-1 1A17 17 0 0 1 3 4a1 1 0 0 1 1-1h3.5a1 1 0 0 1 1 1c0 1.25.2 2.45.57 3.570a1 1 0 0 1-.25 1z" fill="#ffffff"/></svg>
    <span>855-3-FERNWAY</span>
  </div>

  <p class="offer">LOSE 1 LB, GET $20 (UP TO $200)</p>

  <p class="challenge">The challenge is <em>8 weeks</em> long and<br>they must join before March<br><em>31st</em> to be eligible.</p>

  <h2 class="about-title">ABOUT US</h2>
  <div class="about-copy">
    <p>For the past several years we have been developing and working through the concept of a health club that not only rewards its members for exercising, but also follows the global initiative of energy sustainability and Earth friendliness.</p>
    <p>We are the first health club that offers a solution for all of these initiatives all while being a forward-thinking, customer-centric, health and fitness inspiring facility.</p>
  </div>

  <div class="website">
    <svg width="15" height="15" viewBox="0 0 24 24" aria-hidden="true"><g fill="none" stroke="#5cc13c" stroke-width="2"><circle cx="12" cy="12" r="10"/><ellipse cx="12" cy="12" rx="4" ry="10"/><path d="M2 12h20M4 7h16M4 17h16"/></g></svg>
    <span>WWW.FERNWAYFITNESS.COM</span>
  </div>
</main>
</body>
</html>
```